Interfaith Organization needs End of Year Mailing to Supporters

We need to mail out an end of the year appeal to our supporters highlighting our accomplishments and asking for their financial support. The project should be a mix of photos, text, and a space for mailing labels, a return address, and a stamp. We would like it to be 6x9, printed on both sides. We are an interfaith organization that works with students and religious leaders here in Los Angeles, CA.

Target Market(s)

supporters

Industry/Entity Type

Non-Profit

Font styles to use
Serif

Colors

Designer to choose colors to be used in the design.

Requirements
Must have
• an appealing mix of pictures, text, and space for mailing. The flyer should also feature the logos of our various programs.
Nice to have
• make it fun!
Should not have
• boring

```html
<!DOCTYPE html>
<html lang="en">
<head>
<meta charset="utf-8">
<title>Open Circle Alliance – Year-End Appeal Postcard</title>
<link href="https://fonts.googleapis.com/css2?family=Libre+Baskerville:ital,wght@0,700;1,400&family=Source+Sans+3:ital,wght@0,400;0,600;0,700;1,400&display=swap" rel="stylesheet">
<style>
  :root{
    --blue:#3d7fcb;
    --blue-deep:#2f6cb8;
    --blue-light:#dbe8f6;
    --ink:#2b2b2b;
    --ink-soft:#444;
    --link:#2f74c4;
    --white:#ffffff;
    --page:#e6e6e6;
    --rule:rgba(255,255,255,.45);
  }
  *{box-sizing:border-box;margin:0;padding:0}
  html,body{width:1200px;height:1200px;overflow:hidden;background:var(--page)}
  body{position:relative;font-family:"Source Sans 3",Arial,sans-serif;color:var(--ink)}
  .card{position:absolute;left:194px;width:1014px;height:675px;transform:scale(.8);transform-origin:0 0;overflow:hidden;background:var(--white);box-shadow:0 4px 14px rgba(0,0,0,.18)}
  .card--front{top:34px}
  .card--back{top:618px}
  .abs{position:absolute}
  .waves{position:absolute;inset:0;width:1014px;height:675px}
  .hero-photo{left:0;top:0;width:1014px;height:460px;background:linear-gradient(180deg,#c9d2d8 0%,#a9b3ba 22%,#b59f80 36%,#8fcf55 48%,#7bbf48 62%,#8d8a84 80%,#a8a39a 100%)}
  .circle{position:absolute;border-radius:50%;border:6px solid var(--white);box-shadow:0 0 0 5px var(--blue)}
  .circle--team-a{left:607px;top:302px;width:200px;height:200px;background:radial-gradient(circle at 50% 30%,#4fc35b 0%,#3aa24a 40%,#5b5f66 75%,#7a7a7a 100%)}
  .circle--team-b{left:752px;top:392px;width:210px;height:210px;background:linear-gradient(180deg,#d9d6cf 0%,#bdb7ab 40%,#7d7468 70%,#9b948b 100%)}
  .headline{left:48px;top:395px;color:var(--white)}
  .headline__main{font-family:"Libre Baskerville",Georgia,serif;font-weight:700;font-size:37px;line-height:1.1}
  .headline__sub{font-family:"Libre Baskerville",Georgia,serif;font-style:italic;font-size:27px;line-height:1.35}
  .rule{position:absolute;height:1px;background:var(--rule)}
  .intro{left:48px;top:494px;width:600px;color:var(--white);font-size:12.6px;line-height:16px;text-align:justify}
  .ticks{list-style:none;color:var(--white);font-size:13px}
  .ticks li{display:flex;align-items:center;height:19px;white-space:nowrap}
  .ticks svg{width:11px;height:11px;margin-right:7px;flex:none}
  .ticks strong{font-weight:600}
  .ticks em{font-style:italic}
  .globe{display:inline-block;width:12px;height:12px;border:1.5px solid currentColor;border-radius:50%;margin:0 5px 0 6px;vertical-align:-1px}
  .front-list{left:48px;top:585px}
  .back-faint{left:0;top:0;width:565px;height:675px;background:linear-gradient(180deg,#ffffff 0%,#f4f5f6 35%,#eceef0 60%,#e4e7ea 100%)}
  .back-list{left:28px;top:34px;color:var(--ink)}
  .back-list li{height:19px}
  .back-list .url{color:var(--ink-soft);font-style:italic;font-size:12.5px}
  .back-list svg path{stroke:var(--blue)}
  .back-list .globe{color:var(--blue)}
  .section-title{left:29px;top:120px;font-size:16.5px;font-weight:700;color:var(--ink)}
  .projects{left:34px;top:150px;list-style:none;font-size:12.5px}
  .projects li{height:19px;white-space:nowrap;font-weight:700}
  .projects li::before{content:"";display:inline-block;width:4px;height:4px;background:var(--ink);border-radius:50%;margin:0 8px 2px 0}
  .projects a{color:var(--link);text-decoration:none;font-weight:400}
  .impact{left:29px;top:235px;font-size:21.5px;font-weight:700;color:var(--ink)}
  .circle--temple-a{left:42px;top:318px;width:170px;height:170px;background:linear-gradient(180deg,#d6a34b 0%,#b88a52 40%,#6d5a54 70%,#9a2f3b 100%)}
  .circle--temple-b{left:202px;top:278px;width:210px;height:210px;background:linear-gradient(180deg,#4a8fe0 0%,#7db1ec 30%,#d9c8ad 52%,#b39a7b 70%,#5d5a5e 85%,#c3705e 100%)}
  .stamp{left:855px;top:38px;width:109px;height:109px;border:1px solid #bfc3c8}
  .address-line{position:absolute;left:605px;width:359px;height:1px;background:#c9ccd0}
  .appeal{left:29px;top:530px;color:var(--white)}
  .appeal__ask{font-size:19.5px;font-weight:700;line-height:1.15}
  .appeal__note{font-size:13.5px;line-height:1.2}
  .appeal__donate{font-size:17.5px;margin-top:30px}
  .appeal__email{font-size:13.5px;margin-top:2px;display:flex;align-items:center}
  .appeal__email svg{width:28px;height:12px;margin-right:8px}
  .divider{left:414px;top:532px;width:1px;height:110px;background:var(--rule)}
  .contact{left:431px;top:530px;color:var(--white);font-size:12.5px;line-height:16px}
  .contact__row{display:flex;align-items:flex-start}
  .contact__icon{width:12px;height:12px;margin:2px 8px 0 0;flex:none}
  .contact__icon--dot{border:1.5px solid var(--white);border-radius:50%}
  .contact__icon--sq{border:1.5px solid var(--white);border-radius:2px}
  .contact strong{font-weight:700}
  .program-tags{left:640px;top:597px;display:flex;gap:11px}
  .program-tag{width:75px;height:46px;background:var(--white);display:flex;align-items:center;justify-content:center;font-size:13px;font-weight:700;color:var(--blue-deep);text-align:center;line-height:1.05}
  .program-tag--badge{background:#7a7a7a;display:flex;align-items:center;justify-content:center}
  .program-tag--badge span{width:34px;height:34px;border-radius:50%;border:2px solid #d8d8d8}
  .bottom-rule{left:29px;top:656px;width:955px}
</style>
</head>
<body>

<section class="card card--front" aria-label="Postcard front">
  <div class="abs hero-photo" role="img" aria-label="Group photo of students in matching green shirts on a rooftop with the city skyline behind"></div>
  <svg class="waves" viewBox="0 0 1014 675" aria-hidden="true">
    <defs>
      <linearGradient id="frontBlue" x1="0" y1="0" x2="0" y2="1">
        <stop offset="0" stop-color="#4a8ad3"/>
        <stop offset="1" stop-color="#3a78c4"/>
      </linearGradient>
    </defs>
    <path d="M0,350 C190,292 430,300 630,410 C730,462 870,498 1014,462 L1014,482 C870,518 720,486 620,436 C430,336 200,328 0,392 Z" fill="#ffffff" opacity=".75"/>
    <path d="M0,396 C200,334 430,340 620,440 C720,494 870,520 1014,480 L1014,675 L0,675 Z" fill="url(#frontBlue)"/>
  </svg>
  <div class="circle circle--team-a" role="img" aria-label="Photo of students posing in front of a green screen"></div>
  <div class="circle circle--team-b" role="img" aria-label="Photo of students with name badges at a memorial"></div>

  <div class="abs headline">
    <div class="headline__main">OCA hosts 6th year of</div>
    <div class="headline__sub">Youth Interfaith Leadership Program!</div>
  </div>
  <div class="rule" style="left:48px;top:482px;width:590px"></div>

  <p class="abs intro">Open Circle Alliance is in its 6th year of building interfaith leaders here in Los Angeles and Orange County. Our vision is to work with high school and college youth of all religious traditions emphasizing community service, leadership development, and interfaith education. Open Circle Alliance is offering a positive vision of engagement and needs your financial support. This past year we have worked with over 200 students with programs such as:</p>

  <ul class="abs ticks front-list">
    <li><svg viewBox="0 0 12 12"><path d="M1.5,6.5 L4.5,9.5 L10.5,2.5" fill="none" stroke="#fff" stroke-width="2"/></svg><strong>Youth Faith Council of Los Angeles County :</strong><span class="globe"></span><em>www.yfcla-sample.org</em></li>
    <li><svg viewBox="0 0 12 12"><path d="M1.5,6.5 L4.5,9.5 L10.5,2.5" fill="none" stroke="#fff" stroke-width="2"/></svg><strong>Youth Faith Council of Orange County :</strong><span class="globe"></span><em>www.yfcoc-sample.org</em></li>
    <li><svg viewBox="0 0 12 12"><path d="M1.5,6.5 L4.5,9.5 L10.5,2.5" fill="none" stroke="#fff" stroke-width="2"/></svg><strong>Youth Leadership Programs :</strong>&nbsp;<em>Westbrook University, Harlow College,</em>&nbsp;<strong>Bayview State :</strong><span class="globe"></span><em>www.ylp-sample.org</em></li>
  </ul>
  <div class="rule" style="left:48px;top:652px;width:920px"></div>
</section>

<section class="card card--back" aria-label="Postcard back">
  <div class="abs back-faint" role="img" aria-label="Faded photo of a temple courtyard behind the text"></div>

  <ul class="abs ticks back-list">
    <li><svg viewBox="0 0 12 12"><path d="M1.5,6.5 L4.5,9.5 L10.5,2.5" fill="none" stroke-width="2"/></svg>Student Leadership Trips to Washington DC and New Mexico</li>
    <li><svg viewBox="0 0 12 12"><path d="M1.5,6.5 L4.5,9.5 L10.5,2.5" fill="none" stroke-width="2"/></svg>Faith Forum and Festival</li>
    <li><svg viewBox="0 0 12 12"><path d="M1.5,6.5 L4.5,9.5 L10.5,2.5" fill="none" stroke-width="2"/></svg>Shared Roots Peacemaking Initiative :<span class="globe"></span><span class="url">www.sharedrootspeace.org</span></li>
  </ul>

  <h2 class="abs section-title">In addition, OCA also sponsors life-changing projects supporting</h2>
  <ul class="abs projects">
    <li>Rwanda – <a>www.hillsidehope.org,</a></li>
    <li>Pre-school programs in Malawi – <a>www.littlelearners-fund.org,</a></li>
    <li>A film project on Samuel Okafor and forgiveness – <a>www.okaforforgivenessfilm.org</a> ,</li>
    <li>The Arroyo Learning Gardens – <a>www.arroyogardens.org.</a></li>
  </ul>
  <h2 class="abs impact">These projects serve over 2000 people each year!</h2>

  <div class="abs stamp"></div>
  <div class="address-line" style="top:200px"></div>
  <div class="address-line" style="top:240px"></div>
  <div class="address-line" style="top:277px"></div>
  <div class="address-line" style="top:314px"></div>

  <svg class="waves" viewBox="0 0 1014 675" aria-hidden="true">
    <defs>
      <linearGradient id="backBlue" x1="0" y1="0" x2="0" y2="1">
        <stop offset="0" stop-color="#4a8ad3"/>
        <stop offset="1" stop-color="#3a78c4"/>
      </linearGradient>
    </defs>
    <path d="M0,398 C120,375 300,362 420,380 C560,405 700,505 860,506 C930,506 980,488 1014,472 L1014,490 C980,506 930,522 860,522 C700,522 560,420 420,398 C300,380 120,394 0,416 Z" fill="#d6e4f4"/>
    <path d="M0,420 C120,396 300,382 420,400 C560,425 700,528 860,526 C930,524 980,506 1014,492 L1014,675 L0,675 Z" fill="url(#backBlue)"/>
  </svg>

  <div class="circle circle--temple-a" role="img" aria-label="Group photo inside a decorated shrine hall"></div>
  <div class="circle circle--temple-b" role="img" aria-label="Group photo in front of a carved stone temple"></div>

  <div class="abs appeal">
    <div class="appeal__ask">Will you help us meet our goal of $10,000</div>
    <div class="appeal__note">in individual donations to help OCA sustain this needed work?</div>
    <div class="appeal__donate">To donate, please go to PayPort, and give to</div>
    <div class="appeal__email"><svg viewBox="0 0 28 12"><path d="M0,4 H8 M2,8 H8" stroke="#fff" stroke-width="1.2"/><rect x="11" y="1" width="16" height="10" fill="none" stroke="#fff" stroke-width="1.3"/><path d="M11,1 L19,7 L27,1" fill="none" stroke="#fff" stroke-width="1.3"/></svg>give@opencirclealliance.org.</div>
  </div>

  <div class="abs divider"></div>

  <div class="abs contact">
    <div>Or send your donation directly to:</div>
    <div class="contact__row" style="margin-top:4px"><svg class="contact__icon" viewBox="0 0 12 12"><path d="M1,6 L6,1.5 L11,6 M2.5,5 V11 H9.5 V5" fill="none" stroke="#fff" stroke-width="1.5"/></svg><div><strong>Open Circle Alliance</strong><br>1840 E. Orchard Lane, Pasadena, CA 91107<br><strong>(626) 555-0148</strong></div></div>
    <div class="contact__row" style="margin-top:6px"><span class="contact__icon contact__icon--dot"></span>www.opencirclealliance.org</div>
    <div class="contact__row"><span class="contact__icon contact__icon--sq"></span>@OCAnews&nbsp;&nbsp;&nbsp;&nbsp;<span class="contact__icon contact__icon--dot"></span>circlela</div>
  </div>

  <div class="abs program-tags">
    <div class="program-tag">YFC LA</div>
    <div class="program-tag">YLP</div>
    <div class="program-tag">Open<br>Circle</div>
    <div class="program-tag program-tag--badge" role="img" aria-label="Partner badge"><span></span></div>
  </div>

  <div class="rule bottom-rule"></div>
</section>

</body>
</html>
```